Book Cover needed for Printed Book entitled "Step 7"

The Book's Title is "Step 7", the sub-title is "One Resident's Manual on Calm Roadside Stops by Patrol Units", and the author is "Desmond Okafor". The front cover may have just the Title, or it may have a combination of the Title, Sub-Title, and Author. We would like to see designs that presents a feeling of peace and cooperation between US Police Officers and Civilians. The cover can include photographs, illustrations, or just words. But the cover should make the viewer want to open the book for more information.

Target Market(s)

Young adults who live in US inner-cities between ages 18 to 30.

Font styles to use
Sans Serif

Colors

Designer to choose colors to be used in the design.

Requirements
Must have
• Most US Police Officers use the phrase "STEP 7" to tell other officers that the situation is under control and no assistance is needed. And the book will teach Civilians how to safely conduct themselves during police encounters - which will end with the Cops calling in "STEP 7" to the dispatcher. So, the front cover must have the phrase "STEP 7" in big bold letters.
Nice to have
• We would like to see designs that present a feeling of peace and cooperation between US Police Officers and Civilians. Pictures and illustrations of people are acceptable but is not required.

```html
<!DOCTYPE html>
<html lang="en">
<head>
<meta charset="utf-8">
<title>Step 7 — Book Cover</title>
<link rel="stylesheet" href="https://fonts.googleapis.com/css2?family=Oswald:wght@600;700&family=Open+Sans:wght@400;700&display=swap">
<style>
  :root {
    --backdrop-light: #e4f1fa;
    --backdrop-edge: #c5def0;
    --cover-black: #000000;
    --title-yellow: #ffe600;
    --tape-yellow: #f7df12;
    --tape-ink: #111111;
    --subtitle-white: #ffffff;
    --photo-sky: #cfe4f5;
    --photo-blue: #4f8fe0;
    --photo-grey: #c9ccd0;
  }
  * { margin: 0; padding: 0; box-sizing: border-box; }
  html, body { width: 1200px; height: 1200px; overflow: hidden; }
  body {
    background: radial-gradient(circle at 50% 50%, var(--backdrop-light) 0%, var(--backdrop-edge) 100%);
    position: relative;
  }
  .book-cover {
    position: absolute;
    left: 218px; top: 28px;
    width: 762px; height: 1144px;
    background: var(--cover-black);
    overflow: hidden;
    box-shadow: 0 4px 14px rgba(0,0,0,0.25);
  }
  .cover-photo {
    position: absolute;
    left: 0; top: 0;
    width: 762px; height: 480px;
    background:
      linear-gradient(to bottom, rgba(0,0,0,0) 55%, var(--cover-black) 100%),
      radial-gradient(ellipse 60% 14% at 50% 44%, var(--photo-blue) 0%, rgba(79,143,224,0.4) 60%, rgba(79,143,224,0) 100%),
      linear-gradient(to bottom, var(--photo-sky) 0%, #9fc3e6 30%, var(--photo-grey) 60%, #8e9296 80%);
  }
  .title {
    position: absolute;
    left: 0; width: 100%;
    top: 452px;
    text-align: center;
    font-family: "Oswald", sans-serif;
    font-weight: 700;
    font-size: 228px;
    line-height: 1;
    color: var(--title-yellow);
    letter-spacing: 2px;
    transform: scaleX(0.92);
  }
  .tape {
    position: absolute;
    height: 78px;
    background: var(--tape-yellow);
    font-family: "Oswald", sans-serif;
    font-weight: 700;
    color: var(--tape-ink);
    white-space: nowrap;
    display: flex;
    align-items: center;
  }
  .tape--back {
    left: 120px; top: 736px;
    width: 760px;
    font-size: 54px;
    transform: rotate(4deg);
    padding-left: 150px;
  }
  .tape--front {
    left: -20px; top: 660px;
    width: 800px;
    font-size: 56px;
    transform: rotate(-1.6deg);
    padding-left: 60px;
  }
  .subtitle {
    position: absolute;
    left: 0; width: 100%;
    top: 848px;
    text-align: center;
    font-family: "Open Sans", sans-serif;
    font-size: 30px;
    line-height: 35px;
    color: var(--subtitle-white);
    letter-spacing: -0.5px;
  }
  .subtitle strong { font-weight: 700; }
  .author {
    position: absolute;
    left: 0; width: 100%;
    top: 1034px;
    text-align: center;
    font-family: "Open Sans", sans-serif;
    font-weight: 700;
    font-size: 50px;
    color: var(--title-yellow);
    letter-spacing: -1px;
  }
</style>
</head>
<body>
  <main class="book-cover">
    <div class="cover-photo" role="img" aria-label="Photo of a patrol car roof with a blue light bar, street blurred with motion behind it"></div>
    <h1 class="title">STEP 7</h1>
    <div class="tape tape--back">POLICE LINE DO NOT CROSS</div>
    <div class="tape tape--front">POLICE LINE DO NOT CROSS</div>
    <p class="subtitle"><strong>One Resident's Manual</strong> on<br>Calm Roadside Stops by Patrol Units</p>
    <p class="author">Desmond Okafor</p>
  </main>
</body>
</html>
```